Web Design Project

My site is already up - www.brightwell-hub.com but is very basic at this stage.
I need a to make the design look better and lift it a bit.
I have my own ideas about what I want.
The target market for the site is women - mainly professional, corporate women around the world aged between 28-40 yrs or thereabouts.
There are 3 main areas the site will focus on:
1: Blog and Inbox magazine with contributing writers on various topics from food, diet, emotional intelligence, intuition, feminine energy sexual and non, money to name a few.
2. There is an Ebook that is being added to the site later this year taking a deeper look at all of these topics. For now those subscribing get a free summary of the book.
Book called "Marigold - Your Gentle Guide to a Calmer Rhythm"
Happy to use the title for the FREE summary for subscribers.
3. Events / retreats. We are kicking off with our first Brightwell-hub retreat in Bali in late Oct 2012. We have amazing shots of the villa we will use and the activities etc that will make up a part of the retreat.
Yoga & meditation
Surfing
Photography
Keen to see what you all come up with.
NOTE: I dont want anything too busy. Keep it fairly clean, simple and in keeping with the general look and feel right now.
Updates
Target Market(s)
Look and feel
Each slider illustrates characteristics of the customer's brand and the style your logo design should communicate.

```html
<!DOCTYPE html>
<html lang="en">
<head>
<meta charset="utf-8">
<title>Brightwell-hub retreat 2012 Bali</title>
<link rel="stylesheet" href="https://fonts.googleapis.com/css2?family=Noto+Sans:ital,wght@0,400;0,700;1,700&display=swap">
<style>
  :root {
    --canvas: #ffffff;
    --brand-yellow: #f7d800;
    --button-yellow: #f6d400;
    --button-edge: #e2bd00;
    --heading-grey: #8a8a8a;
    --panel-border: #dcdcdc;
    --band-grey: #e4e4e4;
    --band-light: #f1f1f1;
    --text-dark: #1e1e1e;
    --overlay: rgba(40, 30, 20, 0.55);
  }
  * { margin: 0; padding: 0; box-sizing: border-box; }
  html, body {
    width: 1200px; height: 400px; overflow: hidden;
    background: var(--canvas);
    font-family: "Noto Sans", sans-serif;
  }
  .banner { position: relative; width: 1200px; height: 400px; }

  .retreat-feature {
    position: absolute; left: 15px; top: 15px; width: 570px; height: 375px; overflow: hidden;
  }
  .retreat-photo {
    position: absolute; inset: 0;
    background:
      radial-gradient(ellipse at 58% 55%, #8d8376 0%, #5a4a3a 30%, transparent 55%),
      radial-gradient(ellipse at 90% 30%, #e9e2d8 0%, transparent 35%),
      radial-gradient(ellipse at 15% 60%, #cfc6bb 0%, transparent 30%),
      linear-gradient(135deg, #6b4a32 0%, #3b2618 55%, #2a1a10 100%);
  }
  .retreat-title {
    position: absolute; left: 0; top: 12px; width: 100%; height: 57px;
    background: var(--overlay);
    display: flex; align-items: center; padding-left: 23px;
    font-weight: 700; font-size: 29px; color: #ffffff; letter-spacing: 0.3px;
  }
  .retreat-title .brand { color: var(--brand-yellow); margin-right: 10px; }

  .signup-panel {
    position: absolute; left: 630px; top: 15px; width: 555px; height: 375px;
    border: 1px solid var(--panel-border); background: #fff;
  }
  .signup-heading {
    position: absolute; left: 0; top: 28px; width: 100%;
    text-align: center; font-weight: 700; font-size: 30px; line-height: 41px;
    color: var(--heading-grey);
  }
  .signup-heading .brand { color: var(--brand-yellow); }
  .signup-button {
    position: absolute; left: 134px; top: 131px; width: 298px; height: 86px;
    background: var(--button-yellow); border: 2px solid var(--button-edge); border-radius: 4px;
    display: flex; align-items: center; justify-content: center;
    color: #fff; font-weight: 700; font-size: 32px;
    text-shadow: 2px 2px 2px #222, -1px -1px 0 #222, 1px -1px 0 #222, -1px 1px 0 #222;
  }
  .bonus-band {
    position: absolute; left: 14px; top: 242px; width: 526px; height: 115px;
    background: var(--band-grey); overflow: hidden; text-align: center; color: var(--text-dark);
  }
  .bonus-band svg { position: absolute; inset: 0; }
  .bonus-intro { position: relative; margin-top: 8px; font-size: 18px; }
  .bonus-title { position: relative; margin-top: 4px; font-size: 17.5px; font-weight: 700; }
  .bonus-free {
    position: relative; margin-top: 2px; font-size: 33px; font-weight: 700; font-style: italic;
    color: var(--brand-yellow); letter-spacing: 1px;
    text-shadow: 1px 1px 0 #333, -1px -1px 0 #333, 1px -1px 0 #333, -1px 1px 0 #333;
  }
</style>
</head>
<body>
<div class="banner">
  <section class="retreat-feature">
    <div class="retreat-photo" role="img" aria-label="Photo of a silver Buddha head with white orchids, stacked white stones and candles in a spa setting"></div>
    <h1 class="retreat-title"><span class="brand">brightwell-hub</span>retreat 2012 Bali</h1>
  </section>

  <section class="signup-panel">
    <h2 class="signup-heading">Want <span class="brand">brightwell-hub</span> goodness<br>sent straight to your inbox ?</h2>
    <div class="signup-button">Sign up today</div>
    <div class="bonus-band">
      <svg width="526" height="115" viewBox="0 0 526 115" aria-hidden="true">
        <path d="M95 115 C150 40 300 10 526 22 L526 115 Z" fill="var(--band-light)"/>
      </svg>
      <p class="bonus-intro">And receive our bonus Ebook</p>
      <p class="bonus-title">"Marigold - Your Gentle Guide to a Calmer Rhythm"</p>
      <p class="bonus-free">FREE</p>
    </div>
  </section>
</div>
</body>
</html>
```